Looking for a creative label design for our retail coffee bags

We are a coffee manufacturer (coffee roaster) looking to re-brand our retail label for our coffee bags. Our main coffee blend that we sell is our Colombian Supremo Blend. You can use this name when creating the label. We are going for a look that represents our company as a coffee roaster. Please reference our website (www.brindlemoorroasters.com) and our Facebook page to learn more about our company and to give you more inspiration on creating this design.

Target Market(s)

Retail customers/grocery stores

Industry/Entity Type

Manufacturer

Requirements
Must have
• The size of the label has to be 3" width x 4" height

Logo must be Black
Nice to have
• We currently incorporate a color on our labels for each blend. For example, Colombian Supremo Blend (royal blue), Decaffeinated Blend (red), Breakfast Blend (green), Flavored coffees (gold).

Rustic/vintage style

```html
<!DOCTYPE html>
<html lang="en">
<head>
<meta charset="utf-8">
<title>Brindlemoor Roasters – Colombian Supremo Blend Label</title>
<link rel="stylesheet" href="https://fonts.googleapis.com/css2?family=Poppins:wght@300;400;600;700&display=swap">
<style>
  :root {
    --ink: #1e1e1e;
    --paper: #ffffff;
    --roast-red: #970808;
    --bean-dark: #262626;
    --body-font: "Poppins", sans-serif;
  }
  * { margin: 0; padding: 0; box-sizing: border-box; }
  html, body { width: 900px; height: 1200px; overflow: hidden; background: var(--ink); }
  .label {
    position: relative;
    width: 900px;
    height: 1200px;
    overflow: hidden;
    font-family: var(--body-font);
    color: var(--paper);
  }
  .bean-pattern {
    position: absolute;
    inset: 0;
    background: radial-gradient(circle at 50% 50%, var(--bean-dark) 0%, #3a1414 55%, #5a0c0c 100%);
  }
  .label-frame { position: absolute; inset: 0; }
  .brand-name {
    position: absolute;
    left: 286px;
    width: 356px;
    top: 200px;
    text-align: center;
    font-weight: 300;
    font-size: 40px;
    line-height: 52px;
    letter-spacing: 2px;
    color: var(--paper);
  }
  .blend-title {
    position: absolute;
    left: 0;
    width: 910px;
    text-align: center;
    font-weight: 700;
    font-size: 41px;
    line-height: 1;
  }
  .blend-origin { top: 527px; }
  .blend-name { top: 598px; }
  .spec {
    position: absolute;
    left: 122px;
    width: 670px;
    display: flex;
    justify-content: space-between;
    align-items: baseline;
    font-weight: 300;
    font-size: 35px;
    line-height: 1;
  }
  .spec-altitude { top: 700px; }
  .spec-processing { top: 786px; }
  .spec-flavors { top: 873px; }
  .spec-roast { top: 960px; }
  .spec-weight { top: 1047px; }
  .roast-scale {
    position: absolute;
    top: 968px;
    font-weight: 300;
    font-size: 28px;
    line-height: 1;
  }
  .roast-light { left: 283px; }
  .roast-medium { left: 466px; }
  .roast-dark { left: 682px; }
</style>
</head>
<body>
<main class="label">
  <div class="bean-pattern" role="img" aria-label="Repeating pattern of red roasted coffee beans on a dark background"></div>

  <svg class="label-frame" width="900" height="1200" viewBox="0 0 900 1200" aria-hidden="true">
    <path class="info-panel" d="M260 290 H94 V1110 H816 V290 H668 A205 205 0 0 1 260 290 Z"
          fill="var(--ink)" stroke="var(--paper)" stroke-width="4"/>
    <circle class="brand-seal" cx="464" cy="272" r="178" fill="var(--ink)" stroke="var(--paper)" stroke-width="10"/>
    <defs>
      <path id="tagline-arc" d="M294 370 A196 196 0 0 0 634 370"/>
    </defs>
    <text class="brand-tagline" font-family="Poppins, sans-serif" font-size="12.5" font-weight="400"
          letter-spacing="2.2" fill="var(--paper)">
      <textPath href="#tagline-arc" startOffset="50%" text-anchor="middle">PROUDLY ROASTED IN ALDER FALLS, OH SINCE 1994.</textPath>
    </text>
    <rect class="title-rule" x="186" y="577" width="536" height="6" fill="var(--roast-red)"/>
    <g class="spec-dividers" fill="var(--paper)">
      <rect x="122" y="747" width="670" height="3"/>
      <rect x="122" y="834" width="670" height="3"/>
      <rect x="122" y="921" width="670" height="3"/>
      <rect x="122" y="1009" width="670" height="3"/>
    </g>
    <circle class="roast-marker" cx="774" cy="985" r="12" fill="var(--paper)"/>
  </svg>

  <div class="brand-name">BRINDLEMOOR<br>ROASTERS</div>

  <h1 class="blend-title blend-origin">COLOMBIAN</h1>
  <h2 class="blend-title blend-name">SUPREMO BLEND</h2>

  <div class="spec spec-altitude"><span>Altitude:</span><span>1800-1900</span></div>
  <div class="spec spec-processing"><span>Processing:</span><span>Washed</span></div>
  <div class="spec spec-flavors"><span>Flavors:</span><span>Rich aroma</span></div>
  <div class="spec spec-roast"><span>Roast:</span></div>
  <span class="roast-scale roast-light">Light</span>
  <span class="roast-scale roast-medium">Medium</span>
  <span class="roast-scale roast-dark">Dark</span>
  <div class="spec spec-weight"><span>Weight:</span><span>500g</span></div>
</main>
</body>
</html>
```